Health care technology software systems

We have a solid logo. We have company colors that will need to be used as well. We just need a great business card design. We sell to health plans but want to be modern

Target Market(s)

Health technology sector selling into Health Plans

Industry/Entity Type

Health Care Technology

Contact Information for Business Card

Name, title, address, phone number, email

Requirements
Must have
• Use of Parvexa corporate colors - Uploaded w/ our logos

```html
<!DOCTYPE html>
<html lang="en">
<head>
<meta charset="utf-8">
<title>Parvexa Business Card</title>
<link rel="stylesheet" href="https://fonts.googleapis.com/css2?family=Lato:wght@300;400&family=Open+Sans:wght@400;600&display=swap">
<style>
  :root {
    --backdrop: #c4c4c4;
    --card-white: #ffffff;
    --brand-blue: #29a9e1;
    --brand-blue-light: #4fbbea;
    --brand-navy: #3a4f9e;
    --brand-green: #8cc63f;
    --ink: #3b3b3b;
    --ink-soft: #555555;
    --card-black: #141414;
    --card-black-light: #2e2e2e;
  }
  * { box-sizing: border-box; margin: 0; padding: 0; }
  html, body { width: 1200px; height: 876px; overflow: hidden; }
  body {
    background: var(--backdrop);
    display: flex;
    align-items: center;
    justify-content: center;
    gap: 40px;
    font-family: "Open Sans", sans-serif;
  }
  .card {
    position: relative;
    width: 540px;
    height: 309px;
    border-radius: 3px;
    overflow: hidden;
    box-shadow: 0 6px 18px rgba(0,0,0,0.25);
  }
  .card-front { background: var(--card-white); }
  .card-back {
    background: radial-gradient(ellipse at 45% 40%, var(--card-black-light), var(--card-black) 70%);
    display: flex;
    align-items: center;
    justify-content: center;
  }
  .footer-band {
    position: absolute;
    left: 0; right: 0; bottom: 0;
    height: 58px;
    background: linear-gradient(90deg, var(--brand-blue-light), var(--brand-blue));
  }
  .footer-rule {
    position: absolute;
    left: 0; right: 0; bottom: 64px;
    height: 3px;
    background: var(--brand-green);
  }
  .identity { position: absolute; left: 38px; top: 26px; }
  .person-name {
    font-size: 20px;
    font-weight: 400;
    color: var(--brand-blue);
    line-height: 1.1;
  }
  .person-title { font-size: 9.5px; color: var(--ink-soft); margin-top: 3px; }
  .contacts { list-style: none; margin-top: 14px; }
  .contacts li {
    display: flex;
    align-items: center;
    gap: 8px;
    font-size: 10.5px;
    color: var(--ink);
    height: 17px;
  }
  .icon {
    width: 13px; height: 13px;
    border-radius: 2px;
    background: var(--brand-navy);
    display: flex; align-items: center; justify-content: center;
  }
  .icon svg { width: 9px; height: 9px; }
  .address { margin-top: 10px; font-size: 11.5px; color: var(--ink); line-height: 1.35; }
  .wordmark {
    display: flex;
    align-items: center;
    gap: 10px;
    font-family: "Lato", sans-serif;
    font-weight: 300;
  }
  .wordmark-dot { border-radius: 50%; background: var(--brand-blue); }
  .card-front .wordmark {
    position: absolute; right: 40px; top: 118px;
    font-size: 44px; color: var(--ink);
  }
  .card-front .wordmark-dot { width: 24px; height: 24px; }
  .card-back .wordmark { font-size: 62px; color: #f2f2f2; }
  .card-back .wordmark-dot { width: 36px; height: 36px; }
</style>
</head>
<body>

<section class="card card-front">
  <div class="identity">
    <h1 class="person-name">Laura Benton</h1>
    <p class="person-title">Health Care Technology</p>
    <ul class="contacts">
      <li><span class="icon"><svg viewBox="0 0 10 10"><path fill="#fff" d="M2 1l2 0 .6 2-1 1c.5 1 1.3 1.8 2.4 2.4l1-1 2 .6 0 2c-4 .3-7.3-3-7-7z"/></svg></span>+000 123 456 7890</li>
      <li><span class="icon"><svg viewBox="0 0 10 10"><rect x="1" y="2.5" width="8" height="5" fill="none" stroke="#fff"/><path d="M1 2.5l4 3 4-3" fill="none" stroke="#fff"/></svg></span>yourgmail@name.com</li>
      <li><span class="icon"><svg viewBox="0 0 10 10"><circle cx="5" cy="5" r="3.8" fill="none" stroke="#fff"/><path d="M1.2 5h7.6M5 1.2c-2 2.5-2 5 0 7.6M5 1.2c2 2.5 2 5 0 7.6" fill="none" stroke="#fff" stroke-width=".7"/></svg></span>www.websitename.com</li>
    </ul>
    <p class="address">your street address place here<br>new york city, zip code - 000</p>
  </div>

  <div class="wordmark">
    <span class="wordmark-dot"></span>
    <span>parvexa</span>
  </div>

  <div class="footer-rule"></div>
  <div class="footer-band"></div>
</section>

<section class="card card-back">
  <div class="wordmark">
    <span class="wordmark-dot"></span>
    <span>parvexa</span>
  </div>
</section>

</body>
</html>
```